依頼詳細
新規の取引の際にもホームページや会社案内を見て頂き、安心してお取引いただけるようになればと考えております。

日々お客様からご依頼いただき、買い取らせていただいている様々な金属を具体的にホームページに掲載し、こんなものも買い取ってもらえるんだということをお客様に知っていただければと考えております。

個人から個人事業主、法人のお客様の開拓と、栃木県内だけでなくより広範囲のお客様の開拓も行っていきます。

画像等は、有料素材サイトなどからのご提案もお願いいたします。
会社のロゴは、添付のロゴ写真を参考にして下さい。(株)ではなく株式会社にして下さい。フォントは同じようなものでお願いします。
サイトURL
ページ数
1ページ
希望イメージ
シンプル 複雑
単色 カラフル
暗い 明るい
日常 高級
遊び心 厳粛
未来的 伝統的
女性的 男性的
希望する色
青系、ロゴの色をメインカラーにして下さい。
納品ファイル
• 高解像度JPG (.jpg)
• イラストレーター形式 (.ai)
• フォトショップ形式 (.psd)
補足説明
レスポンシブデザインにてご提案をお願い致します。
スマートフォンのデザインもご提示いただければと思います。
お世話になっております。もう提案をいただきたいと思います。
よろしくお願いいたします。
■ 選んだ理由

お客様が大変悩まれておりましたが、素晴らしいデザインといっていただけました。ありがとうございました。今後修正等があるかと思いますが引き続きよろしくお願いします。

■ 提案者全員のお礼・コメント

たくさんのデザインありがとうございました。
お客様も大変悩まれておりました。
今後もデザインコンペを行ってまいりますのでよろしくお願いいたします。

```html
<!DOCTYPE html>
<html lang="ja">
<head>
<meta charset="utf-8">
<title>株式会社東山メタル | 金属・非鉄金属買取</title>
<link href="https://fonts.googleapis.com/css2?family=Noto+Sans+JP:wght@400;500;700&display=swap" rel="stylesheet">
<style>
:root{
  --blue:#1a4f9c;
  --blue-dark:#123a78;
  --blue-light:#2f6cc0;
  --text:#333;
  --muted:#777;
  --line:#d9dde3;
  --gray:#eef0f3;
  --white:#fff;
}
*{margin:0;padding:0;box-sizing:border-box}
html,body{width:1200px;height:4412px;overflow:hidden}
body{font-family:"Noto Sans JP",sans-serif;color:var(--text);font-size:13px;line-height:1.9;background:var(--white)}
.wrap{width:940px;margin:0 auto;position:relative}
/* header */
.site-header{height:92px;background:var(--white)}
.header-top{height:52px;display:flex;justify-content:space-between;align-items:center}
.brand{font-family:"Noto Sans JP",sans-serif;font-weight:700;font-size:18px;color:var(--blue);letter-spacing:1px}
.contact{text-align:right;line-height:1.3}
.contact-label{font-size:10px;color:var(--muted)}
.contact-tel{font-size:20px;font-weight:700;color:var(--blue);display:flex;align-items:center;gap:6px;justify-content:flex-end}
.global-nav{height:40px;border-top:1px solid var(--line);border-bottom:1px solid var(--line)}
.global-nav ul{list-style:none;display:flex;width:940px;margin:0 auto}
.global-nav li{flex:1;text-align:center;line-height:38px;font-size:12px;border-right:1px solid var(--line)}
.global-nav li:first-child{border-left:1px solid var(--line)}
.global-nav li.current{background:var(--blue);color:var(--white)}
/* hero */
.hero{height:500px;position:relative;background:linear-gradient(180deg,#9fc3e6 0%,#dfe8ef 38%,#8c8275 62%,#5d5046 100%)}
.hero-copy{position:absolute;top:70px;left:0;right:0;text-align:center;color:var(--white)}
.hero-title{font-size:46px;font-weight:700;letter-spacing:4px;text-shadow:0 2px 6px rgba(0,0,0,.35)}
.hero-sub{display:inline-block;margin-top:6px;background:rgba(26,79,156,.85);padding:2px 26px;font-size:18px;letter-spacing:2px}
/* section heads */
.sec-title{font-size:22px;font-weight:700;color:var(--text);line-height:1.4}
.sec-en{font-size:10px;color:var(--blue);letter-spacing:2px;font-weight:500}
.head-center{text-align:center;margin-bottom:34px}
.head-center .sec-title{display:inline-block;padding:0 24px}
.head-rule{width:360px;height:1px;background:var(--line);margin:0 auto 10px}
/* commitment */
.commit{height:488px;padding-top:70px}
.commit .wrap{display:flex;justify-content:space-between}
.commit-text{width:440px}
.commit-text p{margin-top:18px}
.commit-photo{width:420px;height:300px;background:radial-gradient(circle at 55% 55%,#e9f7df 0%,#8ccf52 45%,#3e9a2b 100%);margin-top:10px}
/* about */
.about{height:480px;padding-top:30px}
.about .wrap{display:flex;justify-content:space-between}
.about-circles{width:420px;height:400px;position:relative}
.about-circles span{position:absolute;border-radius:50%}
.c1{width:210px;height:210px;left:10px;top:0;background:radial-gradient(#f2f2f2,#9a9fa6)}
.c2{width:190px;height:190px;left:220px;top:40px;background:radial-gradient(#f3d08b,#b07a2a)}
.c3{width:170px;height:170px;left:40px;top:215px;background:radial-gradient(#bfc7d1,#5c6775)}
.c4{width:180px;height:180px;left:215px;top:225px;background:radial-gradient(#f0a56e,#a34c1e)}
.about-text{width:460px;padding-top:40px}
.about-text p{margin-top:16px}
/* results */
.results{height:1180px;background:linear-gradient(160deg,var(--blue-light),var(--blue-dark));padding-top:70px}
.results .sec-title,.results .sec-en{color:var(--white)}
.results .head-rule{background:rgba(255,255,255,.4)}
.card-grid{display:grid;grid-template-columns:repeat(3,290px);gap:50px 35px;justify-content:center}
.case-card{background:var(--white)}
.case-photo{height:250px}
.p1{background:linear-gradient(135deg,#b7bcc2,#5d646c)}
.p2{background:linear-gradient(135deg,#d7e3f0,#6f8ba8)}
.p3{background:linear-gradient(135deg,#e6a070,#8a3f18)}
.p4{background:linear-gradient(135deg,#cfd3d8,#6a7079)}
.p5{background:linear-gradient(135deg,#9aa0a8,#3e444c)}
.p6{background:linear-gradient(135deg,#c8dff5,#3b6ea8)}
.case-body{padding:16px 22px 22px;height:170px}
.case-body h3{text-align:center;font-size:14px;color:var(--blue);margin-bottom:8px}
.case-body p{font-size:12px;line-height:1.8}
/* faq */
.faq{height:580px;padding-top:60px}
.faq-list{width:900px;margin:0 auto}
.faq-item{border-bottom:1px solid var(--line);padding:14px 0}
.faq-q{display:flex;align-items:center;gap:12px;color:var(--blue);font-weight:700;font-size:15px}
.q-icon{width:26px;height:26px;background:var(--blue);color:var(--white);display:flex;align-items:center;justify-content:center;font-size:13px;flex:none}
.faq-a{padding:6px 0 0 38px;font-size:12px}
/* buy list */
.buy{height:600px;background:var(--gray);padding-top:60px}
.buy .head-rule{background:#c8cdd4}
.buy-grid{display:grid;grid-template-columns:repeat(2,440px);gap:36px 60px;justify-content:center}
.buy-card{background:var(--white)}
.buy-card h3{background:var(--blue);color:var(--white);text-align:center;font-size:15px;line-height:44px}
.buy-card p{padding:18px 24px;font-size:12px;height:130px}
/* news */
.news{height:380px;padding-top:50px}
.news-list{width:900px;margin:0 auto;list-style:none}
.news-list li{display:flex;line-height:46px;border-bottom:1px solid var(--line)}
.news-list li:nth-child(odd){background:var(--gray)}
.news-date{width:150px;padding-left:24px;color:var(--muted)}
.news-text{color:var(--blue)}
/* footer */
.site-footer{height:112px}
.footer-nav{height:70px;display:flex;justify-content:center;align-items:center;list-style:none;font-size:12px}
.footer-nav li{padding:0 16px;border-left:1px solid var(--line);line-height:1}
.footer-nav li:first-child{border-left:none}
.copyright{height:42px;background:var(--blue);color:var(--white);text-align:center;line-height:42px;font-size:11px}
</style>
</head>
<body>
<header class="site-header">
  <div class="wrap header-top">
    <div class="brand">株式会社東山メタル</div>
    <div class="contact">
      <div class="contact-label">お見積り・お問い合わせはこちら</div>
      <div class="contact-tel">
        <svg width="18" height="18" viewBox="0 0 24 24" aria-hidden="true"><path fill="#1a4f9c" d="M6.6 10.8a15 15 0 0 0 6.6 6.6l2.2-2.2c.3-.3.7-.4 1-.2 1.1.4 2.3.6 3.6.6.6 0 1 .4 1 1V20c0 .6-.4 1-1 1A17 17 0 0 1 3 4c0-.6.4-1 1-1h3.5c.6 0 1 .4 1 1 0 1.3.2 2.5.6 3.6.1.3 0 .7-.2 1z"/></svg>
        0120-00-0000
      </div>
    </div>
  </div>
  <nav class="global-nav">
    <ul>
      <li class="current">HOME</li><li>当社について</li><li>買取の流れ</li><li>買取品目</li><li>会社概要</li><li>お問い合わせ</li>
    </ul>
  </nav>
</header>

<section class="hero" role="img" aria-label="積み上げられた金属スクラップと青空の写真">
  <div class="hero-copy">
    <h1 class="hero-title">迅速対応、完璧な仕事</h1>
    <p class="hero-sub">金属・非鉄金属買取致します</p>
  </div>
</section>

<section class="commit">
  <div class="wrap">
    <div class="commit-text">
      <h2 class="sec-title">当社のこだわり</h2>
      <div class="sec-en">COMMITMENT</div>
      <p>金属（スクラップ）の買取を行っております。お持ち込みいただいた金属は、専門のスタッフが一点ずつ丁寧に確認し、適正な価格でお買い取りいたします。少量からでもお気軽にご相談ください。</p>
      <p>金属（スクラップ）の買取を通じて、資源の再利用と地域の環境づくりに取り組んでいます。個人のお客様から法人のお客様まで、安心してお取引いただける体制を整えております。</p>
      <p>お客様に満足していただけるよう、迅速な対応と分かりやすいご説明を心がけております。</p>
    </div>
    <div class="commit-photo" role="img" aria-label="緑の葉と地球のイメージ写真"></div>
  </div>
</section>

<section class="about">
  <div class="wrap">
    <div class="about-circles" role="img" aria-label="アルミ、真鍮、鉄、銅など金属素材の丸い写真">
      <span class="c1"></span><span class="c2"></span><span class="c3"></span><span class="c4"></span>
    </div>
    <div class="about-text">
      <h2 class="sec-title">買取について</h2>
      <div class="sec-en">ABOUT PURCHASE</div>
      <p>金属（スクラップ）の買取を行っております。鉄・銅・真鍮・アルミ・ステンレスなど、様々な金属を取り扱っております。ご不明な点はお気軽にお問い合わせください。</p>
      <p>金属の種類や状態により買取価格は異なります。お電話でのお見積りも承っておりますので、まずはお気軽にご連絡ください。</p>
      <p>大量のお持ち込みや出張での引き取りにも対応しております。県内だけでなく、広い地域のお客様からのご依頼をお待ちしております。</p>
    </div>
  </div>
</section>

<section class="results">
  <div class="head-center">
    <div class="head-rule"></div>
    <h2 class="sec-title">買取実績</h2>
    <div class="sec-en">PURCHASE RECORD</div>
  </div>
  <div class="card-grid">
    <article class="case-card"><div class="case-photo p1" role="img" aria-label="金属部品の写真"></div><div class="case-body"><h3>事例紹介</h3><p>金属（スクラップ）の買取事例です。使用済みの部品を多数お持ち込みいただき、状態を確認のうえ適正価格でお買い取りしました。</p></div></article>
    <article class="case-card"><div class="case-photo p2" role="img" aria-label="アルミ片の写真"></div><div class="case-body"><h3>事例紹介</h3><p>金属（スクラップ）の買取事例です。工場から出たアルミ片をまとめてお持ち込みいただき、迅速にお買い取りしました。</p></div></article>
    <article class="case-card"><div class="case-photo p3" role="img" aria-label="銅管の写真"></div><div class="case-body"><h3>事例紹介</h3><p>金属（スクラップ）の買取事例です。解体現場から出た銅管を出張で引き取り、その場でお見積りをいたしました。</p></div></article>
    <article class="case-card"><div class="case-photo p4" role="img" aria-label="機械部品の写真"></div><div class="case-body"><h3>事例紹介</h3><p>金属（スクラップ）の買取事例です。不要になった機械部品を分別し、素材ごとに適正な価格でお買い取りしました。</p></div></article>
    <article class="case-card"><div class="case-photo p5" role="img" aria-label="金属素材の写真"></div><div class="case-body"><h3>事例紹介</h3><p>金属（スクラップ）の買取事例です。個人のお客様から少量のお持ち込みをいただき、丁寧に査定いたしました。</p></div></article>
    <article class="case-card"><div class="case-photo p6" role="img" aria-label="金属片の写真"></div><div class="case-body"><h3>事例紹介</h3><p>金属（スクラップ）の買取事例です。法人のお客様より定期的なご依頼をいただき、継続してお取引しております。</p></div></article>
  </div>
</section>

<section class="faq">
  <div class="head-center">
    <div class="head-rule"></div>
    <h2 class="sec-title">買取のよくある質問</h2>
    <div class="sec-en">FAQ</div>
  </div>
  <div class="faq-list">
    <div class="faq-item"><div class="faq-q"><span class="q-icon">Q</span>金属（スクラップ）は何でも買い取ってもらえますか？</div><p class="faq-a">金属（スクラップ）の種類や状態によって異なります。まずはお電話またはお問い合わせフォームからお気軽にご相談ください。専門スタッフがお答えいたします。</p></div>
    <div class="faq-item"><div class="faq-q"><span class="q-icon">Q</span>買取価格を教えてください</div><p class="faq-a">買取価格は相場や品目により変動いたします。お電話でのお見積りも承っておりますので、品目と量をお知らせください。</p></div>
    <div class="faq-item"><div class="faq-q"><span class="q-icon">Q</span>金属（スクラップ）は少量でも買い取ってもらえますか？</div><p class="faq-a">少量からでもお買い取りいたします。個人のお客様のお持ち込みも歓迎しておりますので、お気軽にお越しください。</p></div>
    <div class="faq-item"><div class="faq-q"><span class="q-icon">Q</span>出張での引き取りはできますか？</div><p class="faq-a">大量の金属や大型のものは出張での引き取りにも対応しております。日程や地域についてはご相談ください。</p></div>
  </div>
</section>

<section class="buy">
  <div class="head-center">
    <div class="head-rule"></div>
    <h2 class="sec-title">買い取れるもの</h2>
    <div class="sec-en">PURCHASE LIST</div>
  </div>
  <div class="buy-grid">
    <div class="buy-card"><h3>金属の説明</h3><p>鉄（スクラップ）の買取を行っております。建築廃材や機械部品など、様々な鉄製品をお買い取りいたします。状態を確認のうえ、適正価格をご提示いたします。</p></div>
    <div class="buy-card"><h3>金属の説明</h3><p>銅（スクラップ）の買取を行っております。電線や銅管、銅板など幅広く取り扱っております。被覆の有無により価格が異なりますのでご相談ください。</p></div>
    <div class="buy-card"><h3>金属の説明</h3><p>アルミ（スクラップ）の買取を行っております。サッシやアルミ缶、加工くずなどもお買い取りいたします。少量からお気軽にお持ち込みください。</p></div>
    <div class="buy-card"><h3>金属の説明</h3><p>真鍮・ステンレス（スクラップ）の買取を行っております。バルブや部品、厨房機器などもお買い取りいたします。まずはお問い合わせください。</p></div>
  </div>
</section>

<section class="news">
  <div class="head-center">
    <div class="head-rule"></div>
    <h2 class="sec-title">新着情報</h2>
    <div class="sec-en">NEWS</div>
  </div>
  <ul class="news-list">
    <li><span class="news-date">2017.07.20</span><span class="news-text">金属（スクラップ）の買取価格を更新しました。</span></li>
    <li><span class="news-date">2017.07.20</span><span class="news-text">ご依頼の多い金属の買取事例を追加しました。</span></li>
    <li><span class="news-date">2017.07.20</span><span class="news-text">夏季休業期間のお知らせを掲載しました。</span></li>
    <li><span class="news-date">2017.07.20</span><span class="news-text">出張引き取りの対応地域を拡大いたしました。</span></li>
    <li><span class="news-date">2017.07.20</span><span class="news-text">ホームページをリニューアルいたしました。</span></li>
  </ul>
</section>

<footer class="site-footer">
  <ul class="footer-nav">
    <li>HOME</li><li>当社について</li><li>買取の流れ</li><li>買取品目</li><li>会社概要</li><li>お問い合わせ</li>
  </ul>
  <div class="copyright">Copyright © 2017 株式会社東山メタル All Rights Reserved.</div>
</footer>
</body>
</html>
```